Molveta - Customer Experience Software Company Web Design

*****UPDATE*****
We've been getting a lot of corporate designs through. Unfortunately this is not what we are looking for. We would like our brand to be more approachable and for the look and feel to to be a bit more fun.
Also the best designs we have received so far have followed the "less is more" approach. Im hoping any news designs will take these aspects into account.
*****************

Background:

Molveta is a Customer Experience Technology company. We equip business and technology teams with the frameworks, tools and services to help them create compelling experiences for their customers.

Our flagship product - Molveta CX is an open-source customer experience application framework – it enables organisation to build highly differentiated business applications to deliver compelling experiences to your customers.

Molveta CX is designed for innovators who understand that unlocking opportunity in today’s competitive marketplace is driven by delivering a better customer experience.

Task:

We are looking for a web design (we need PSD, no HTML/CSS) for our company site through which to launch our customer experience framework product. The site will be also used as a support site, so the functional aspect of the site is as important as the visual impact for sales.

In order to help us conceptualise ideas and content we have drafted a temporary website using a standard wordpress theme (please see details below). Now we have a general idea of our requirements we like we would like to take it to the next level and get some designs with that professional edge.

Our target market are Enterprise organisations - that is senior members of the business & technology teams (Business General Managers, CTO’s, CIO’s, and Senior Architects and Senior Developers). We want something clean & fresh which is DIFFERENT from the typical corporate technology websites out there. We would like to be seen as more approachable than most large technology companies.

Words we would like to use to describe the finished design:
• Clean (we’re thinking white background with one or two key colours)
• Fresh
• Light
• Modern
• Less is more
• Web 2.0
• Fun but professional (aimed at Enterprise/Large organisations)
• Bold, clear call to action – e.g. Live Demo & Download
• Readable (but Sans Serif)

As we’re a Customer Experience company, the usability of the site is critical. The site must be functional, intuitive & easy to navigate. We want to keep the number of user clicks to the bare minimum possible.

Other aspects, which we would like to incorporate into the site
• Home Page banner slider
• Client logon
• Newsletter sign up
• Social media links – Friendloop, Careerweave (for starters)
• Rich footer links

Some websites we like
• http://brightpanelworks.com - clean, light, modern & intuitive
• http://www.tamsinvoroley.com - bold, clear messaging
• http://www.qz5.net/html/logo - punchy, colourful
• http://parcelwren.com/ - modern, clear messaging, colourful, rich footer area

Target Market(s)

Enterprise organisations - that is senior members of the business & technology teams (Business General Managers, CTO’s, CIO’s, Senior Devs)

Industry/Entity Type

Business

Requirements
Must have
• - Design Specs: Accepted file formats: During the design phase adobe PSD or JPEG are OK (if you need to upload files), but for the handover we'll need PSD only with all the original layers.
- The width needs to be a size that will work with every size computer screen
- Need to use cross-platform compatible font
- The graphic elements used for the design must be copyright free

Current test site
- URL http://molveta.com/wp-admin
- username: artfolkhub
- password: artfolkhub

IMPORTANT NOTE REGARDING OUR CURRENT TEST SITE:

This is a very basic version of a site to help us generate requirements. This design is only a starting point/input and is not locked in stone i.e. we do not simply want this site simply tweaked around the edges.

We are looking for you to use all of your graphic design skills and experience to create a truly awesome site design!

```html
<!DOCTYPE html>
<html lang="en">
<head>
<meta charset="utf-8">
<title>Molveta — Customer Experience Application Framework</title>
<link rel="stylesheet" href="https://fonts.googleapis.com/css2?family=Graduate&family=Marcellus&display=swap">
<style>
  :root {
    --header-top: #f4f4f4;
    --header-bottom: #dedede;
    --ink: #111111;
    --ink-soft: #333333;
    --muted: #9a9a9a;
    --headline: #535353;
    --band: #333333;
    --section: #dcdcdc;
    --footer: #ececec;
    --rule: #c9c9c9;
    --slider-frame: #6f7378;
    --slider-bar-top: #d3d9e1;
    --slider-bar-bottom: #a8b1bd;
    --dot: #2b2f36;
    --dot-active: #e9edf2;
    --button-top: #fbfbfb;
    --button-bottom: #d9d9d9;
    --pill: #3a3d42;
    --white: #ffffff;
  }
  * { box-sizing: border-box; margin: 0; padding: 0; }
  html, body { width: 1098px; height: 1200px; overflow: hidden; background: var(--white); }
  body { position: relative; font-family: Arial, Helvetica, sans-serif; color: var(--ink); }

  .site-header {
    position: absolute; left: 0; top: 0; width: 1098px; height: 45px;
    background: linear-gradient(var(--header-top), var(--header-bottom));
    border-bottom: 1px solid #cfcfcf;
  }
  .brand { position: absolute; left: 41px; top: 11px; font-size: 20px; font-weight: 700; color: var(--ink); }
  .main-nav a, .account-nav a {
    position: absolute; top: 20px; font-size: 10px; font-weight: 700; text-decoration: none; color: var(--ink);
  }
  .main-nav .current { color: var(--muted); border-bottom: 1px solid var(--muted); }
  .account-nav a { color: var(--muted); font-weight: 400; }

  .slider {
    position: absolute; left: 211px; top: 78px; width: 676px; height: 288px;
    border: 2px solid var(--slider-frame); border-radius: 5px; background: var(--white); padding: 3px;
  }
  .slide {
    width: 666px; height: 243px; border-radius: 6px;
    background: radial-gradient(ellipse at 30% 45%, #3a2a4a 0%, #0a0a0a 35%, #000 100%);
  }
  .slider-bar {
    position: absolute; left: 3px; right: 3px; bottom: 3px; height: 33px;
    background: linear-gradient(var(--slider-bar-top), var(--slider-bar-bottom)); border-radius: 0 0 4px 4px;
  }
  .slider-dots { position: absolute; right: 20px; top: 11px; display: flex; gap: 8px; }
  .slider-dots span { width: 9px; height: 9px; border-radius: 50%; background: var(--dot); }
  .slider-dots span:first-child { background: var(--dot-active); border: 1px solid #8c949e; }

  .band { position: absolute; left: 0; top: 391px; width: 1098px; height: 12px; background: var(--band); }

  .intro {
    position: absolute; left: 0; top: 403px; width: 1098px; height: 636px;
    background: repeating-linear-gradient(90deg, #dadada 0 2px, #dedede 2px 4px);
  }
  .tagline {
    position: absolute; left: 0; top: 19px; width: 1098px; text-align: center;
    font-family: "Graduate", serif; color: var(--headline); font-size: 40px; line-height: 72px; letter-spacing: 1px;
  }
  .tagline .cap { font-size: 58px; }

  .cta { position: absolute; left: 135px; top: 317px; }
  .button {
    display: inline-block; height: 32px; line-height: 30px; padding: 0 16px; margin-right: 4px;
    border: 1px solid #b4b4b4; border-radius: 6px;
    background: linear-gradient(var(--button-top), var(--button-bottom));
    font-size: 16px; font-weight: 700; color: var(--ink); text-decoration: none;
  }
  .button.demo { width: 111px; text-align: center; padding: 0; }
  .button.buy { width: 59px; text-align: center; padding: 0; }
  .trial { margin-top: 11px; margin-left: 8px; font-size: 11px; line-height: 15px; font-variant: small-caps; color: var(--ink); }
  .trial a { color: var(--ink); }

  .divider { position: absolute; left: 395px; top: 212px; width: 1px; height: 380px; background: linear-gradient(transparent, #c4c4c4 15%, #c4c4c4 85%, transparent); }

  .features { position: absolute; left: 420px; top: 210px; width: 515px; }
  .features h2 {
    font-family: "Marcellus", serif; font-weight: 400; color: var(--ink); font-size: 26px; line-height: 36px;
  }
  .features h3 {
    font-family: "Marcellus", serif; font-weight: 400; color: var(--ink); font-size: 19px; line-height: 28px;
  }
  .features p { font-size: 9.6px; line-height: 11px; color: var(--ink-soft); margin: 17px 0 24px; }

  .site-footer {
    position: absolute; left: 0; top: 1039px; width: 1098px; height: 161px;
    background: var(--footer); border-top: 1px dashed var(--rule);
  }
  .footer-col { position: absolute; top: 20px; }
  .footer-col h4 { font-size: 20px; font-weight: 400; color: var(--ink); margin-bottom: 8px; }
  .footer-col ul { list-style: none; }
  .footer-col li { font-size: 12px; line-height: 14.6px; }
  .footer-col a { color: var(--ink); text-decoration: none; }
  .col-brand { left: 42px; }
  .col-start { left: 202px; }
  .col-support { left: 429px; }
  .col-news { left: 591px; top: 14px; }
  .col-follow { left: 969px; top: 14px; }
  .col-news h4, .col-follow h4 { margin-bottom: 6px; }
  .email-field {
    display: block; width: 235px; height: 21px; border: 1px solid #d6d6d6; background: var(--white);
    font-size: 9px; line-height: 19px; padding-left: 12px; color: var(--ink);
  }
  .subscribe {
    display: block; margin-top: 7px; width: 103px; height: 16px; border-radius: 8px;
    background: linear-gradient(#55595f, var(--pill)); color: var(--white); font-size: 10px; line-height: 16px; text-align: center;
  }
  .social li { display: flex; align-items: center; gap: 6px; margin-bottom: 6px; font-size: 12px; }
  .social .mark { width: 20px; height: 20px; border-radius: 3px; background: #3a6ea5; }
  .col-rule { position: absolute; top: 20px; width: 1px; height: 120px; background: #dcdcdc; }
</style>
</head>
<body>

<header class="site-header">
  <div class="brand">Molveta</div>
  <nav class="main-nav">
    <a class="current" href="#" style="left:567px">HOME</a>
    <a href="#" style="left:611px">PRODUCTS</a>
    <a href="#" style="left:679px">SUPPORT</a>
    <a href="#" style="left:739px">BLOG</a>
    <a href="#" style="left:783px">ABOUT</a>
  </nav>
  <nav class="account-nav">
    <a href="#" style="left:946px">SIGN UP</a>
    <a href="#" style="left:1001px">LOG IN</a>
  </nav>
</header>

<section class="slider">
  <div class="slide" role="img" aria-label="Banner slide: a desktop monitor beside a colourful 3D bar chart and pie chart on black"></div>
  <div class="slider-bar">
    <div class="slider-dots"><span></span><span></span><span></span><span></span><span></span><span></span><span></span><span></span><span></span></div>
  </div>
</section>

<div class="band"></div>

<section class="intro">
  <h1 class="tagline">"<span class="cap">T</span>he customer experience<br><span class="cap">a</span>pplication framework"</h1>

  <div class="cta">
    <a class="button demo" href="#">Live Demo</a><a class="button buy" href="#">Buy</a>
    <p class="trial">30-day <a href="#">FREE</a> trial for Panelix<br>Also Available <a href="#">For Orchard OS</a></p>
  </div>

  <div class="divider"></div>

  <div class="features">
    <h2>Creat compelling experiences for your customers</h2>
    <p>Lorem ipsum dolor sit amet, consec tetuer adipiscing elit. Praesent vestibulum molestie lacus. Aenean nonummy hen drerit mauris. Phasellus porta. Fusce suscipit varius mi. Cum sociis natoque read our.Lorem ipsum dolor sit amet, consec tetuer adipiscing elit. Praesent vestibulum molestie lacus. Aenean nonummy hen drerit mauris. Phasellus porta. Fusce suscipit varius mi. Cum sociis natoque read our.Lorem ipsum dolor sit amet, consec tetuer adipiscing elit. Praesent vestibulum molestie lacus. Aenean nonummy hen drerit mauris. Phasellus porta. Fusce suscipit varius mi. Cum sociis natoque read our.</p>
    <h3>Opportunity through customer experience innovation</h3>
    <p>Lorem ipsum dolor sit amet, consec tetuer adipiscing elit. Praesent vestibulum molestie lacus. Aenean nonummy hen drerit mauris. Phasellus porta. Fusce suscipit varius mi. Cum sociis natoque read our.Lorem ipsum dolor sit amet, consec tetuer adipiscing elit. Praesent vestibulum molestie lacus. Aenean nonummy hen drerit mauris. Phasellus porta. Fusce suscipit varius mi. Cum sociis natoque read our.Lorem ipsum dolor sit amet, consec tetuer adipiscing elit. Praesent vestibulum molestie lacus. Aenean nonummy hen drerit mauris. Phasellus porta. Fusce suscipit varius mi. Cum sociis natoque read our.</p>
    <h3>True difference</h3>
    <p>Lorem ipsum dolor sit amet, consec tetuer adipiscing elit. Praesent vestibulum molestie lacus. Aenean nonummy hen drerit mauris. Phasellus porta. Fusce suscipit varius mi. Cum sociis natoque read our.Lorem ipsum dolor sit amet, consec tetuer adipiscing elit. Praesent vestibulum molestie lacus. Aenean nonummy hen drerit mauris. Phasellus porta. Fusce suscipit varius mi. Cum sociis natoque read our.Lorem ipsum dolor sit amet, consec tetuer adipiscing elit. Praesent vestibulum molestie lacus. Aenean nonummy hen drerit mauris. Phasellus porta. Fusce suscipit varius mi. Cum sociis natoque read our.</p>
  </div>
</section>

<footer class="site-footer">
  <div class="footer-col col-brand">
    <h4>Molveta</h4>
    <ul><li><a href="#">Home</a></li><li><a href="#">Products</a></li><li><a href="#">Support</a></li><li><a href="#">Blog</a></li><li><a href="#">About</a></li></ul>
  </div>
  <div class="footer-col col-start">
    <h4>Getting Started</h4>
    <ul><li><a href="#">Demo</a></li><li><a href="#">Documentation</a></li><li><a href="#">Download</a></li></ul>
  </div>
  <div class="footer-col col-support">
    <h4>Support</h4>
    <ul><li><a href="#">Contact Us</a></li><li><a href="#">Molveta Services</a></li><li><a href="#">Molveta Support</a></li></ul>
  </div>
  <div class="col-rule" style="left:550px"></div>
  <div class="footer-col col-news">
    <h4>Subscribe to our newsletter</h4>
    <span class="email-field">Email Address</span>
    <span class="subscribe">Subscribe</span>
  </div>
  <div class="footer-col col-follow">
    <h4>Follow Us</h4>
    <ul class="social">
      <li><span class="mark"></span>Careerweave</li>
      <li><span class="mark"></span>Friendloop</li>
    </ul>
  </div>
</footer>

</body>
</html>
```